Could You Go Solo Tomorrow? Podcast

We need a "Podcast Cover" for inclusion on Tunora and wavepocket along with a matching or complimentary banner to be included on a landing page which will be hosted on Castlyn (a Castlyn template). The Podcast is called the "Could You Go Solo Tomorrow?" Podcast and has a tag line of "listen before you leap".

I've included an image for a bit of inspiration that shows a person ready to leap into the unknown which, in our podcast, is like a metaphor for launching a business. You may use the photo in your design if you wish or do something completely different including "cartoon" characters or simply text.

Target Market(s)

People who are thinking about starting a new business or buying an existing business and whom have never owned a business before.

Industry/Entity Type

Startup

Font styles to use
Sans Serif

Colors

Designer to choose colors to be used in the design.

Requirements
Must have
• incorporate the "listen before you leap" tagline.

```html
<!DOCTYPE html>
<html lang="en">
<head>
<meta charset="utf-8">
<title>Could You Go Solo Tomorrow? Podcast – Cover</title>
<link rel="stylesheet" href="https://fonts.googleapis.com/css2?family=Open+Sans:wght@600;700&family=Permanent+Marker&display=swap">
<style>
  :root {
    --sun-yellow: #f6c935;
    --haze-light: #f4eba8;
    --haze-mid: #d9c46a;
    --haze-deep: #9a8a3c;
    --ink: #161616;
    --paper: #ffffff;
    --page-bg: #e4e6ea;
  }
  html, body {
    margin: 0;
    width: 1200px;
    height: 1200px;
    overflow: hidden;
    background: var(--page-bg);
  }
  .cover {
    position: relative;
    width: 1200px;
    height: 1200px;
    overflow: hidden;
    font-family: "Open Sans", Arial, sans-serif;
  }
  .cover-photo {
    position: absolute;
    inset: 0;
    background:
      radial-gradient(ellipse 45% 30% at 60% 28%, #fff6c8 0%, rgba(255,246,200,0) 70%),
      linear-gradient(180deg, var(--haze-light) 0%, var(--haze-mid) 45%, var(--haze-deep) 100%);
  }
  .cover-frame {
    position: absolute;
    left: 62px;
    top: 57px;
    right: 59px;
    bottom: 59px;
    border: 7px solid var(--paper);
  }
  .artwork {
    position: absolute;
    inset: 0;
  }
  .title-lead {
    font-weight: 600;
    font-size: 36px;
    fill: var(--ink);
  }
  .tagline {
    font-weight: 700;
    font-size: 38px;
    fill: var(--sun-yellow);
  }
  .title-main {
    position: absolute;
    left: 60px;
    top: 420px;
    width: 1080px;
    margin: 0;
    text-align: center;
    font-family: "Permanent Marker", "Comic Sans MS", cursive;
    font-weight: 400;
    font-size: 178px;
    line-height: 1;
    color: var(--ink);
    text-shadow: -10px 8px 0 var(--paper);
    transform: rotate(-4deg);
  }
  .social-handle {
    position: absolute;
    left: 445px;
    top: 1008px;
    display: flex;
    align-items: center;
    gap: 14px;
    font-weight: 600;
    font-size: 26px;
    color: var(--paper);
  }
  .social-dot {
    width: 56px;
    height: 56px;
    border-radius: 50%;
    background: var(--ink);
  }
</style>
</head>
<body>
  <main class="cover">
    <div class="cover-photo" role="img" aria-label="Sun-washed yellow photo of a city skyline seen from a rooftop edge, a woman in a yellow top leading the viewer by the hand toward the drop"></div>
    <div class="cover-frame"></div>

    <svg class="artwork" width="1200" height="1200" viewBox="0 0 1200 1200" aria-hidden="false">
      <g class="title-banner">
        <polygon points="376,289 832,289 812,318 832,348 376,348 396,318" fill="var(--sun-yellow)"/>
        <text class="title-lead" x="604" y="331" text-anchor="middle">Could You Go Solo</text>
      </g>
      <g class="tagline-ribbon">
        <path d="M240,700 L290,668 Q540,610 820,612 L832,660 Q560,660 296,728 L268,716 Z" fill="var(--ink)"/>
        <path id="tagline-curve" d="M300,705 Q560,640 825,640" fill="none"/>
        <text class="tagline"><textPath href="#tagline-curve" startOffset="50%" text-anchor="middle">listen before you leap</textPath></text>
      </g>
    </svg>

    <h1 class="title-main">Tomorrow?</h1>

    <div class="social-handle">
      <span class="social-dot"></span>
      <span>Friendnest/your fanpage</span>
    </div>
  </main>
</body>
</html>
```